Stationery for London Estate Agents (Real Estate)

We are a modern and professional Estate Agency (Realtors) working with high quality properties in London.
We wish to redesign our stationary using our branding displayed on the front of our offices and require a digital version of this logo to be produced (photograph attached). Slight 'tweaking' of this branding is acceptable.
Updates
1st July 2010 Thank you all those designers who have uploaded submissions. Business Card - Details Side: Business Card - Logo Side: Outline of London Skyline Examples of the london skyline are available at http://www.pictovantix.com/searchkwy_london-skyline-silhouette Please be advised that we are looking for an outline, not a 'filled in' silhouette. Letterhead Please feel free to ask us any questions. Bertrand
I have been able to further refine our design requirements based on your submissions.
We like Pale Forks' business card submission that has not been eliminated and have the following design clarifications;
a) Please use an email icon (e.g an envelope).
b) Please make the email as equally prominent as the telephone and fax
c) We very much like VelloTrine's 'mini window icon' - please display the website URL under such a mini window icon at the bottom right of the card.
We are very happy with the colouring, fonts and proportions used by Pale Forks.
We invite designers to try adding an outline of the London Skyline to the left of the large window icon on the business card and in a suitablie position on the Letterhead (e.g at the top left of the letterhead).
We have the following design clarifiications to our Letterhead requirements;
A) We would like the main logo to be on the top right side of the letterhead.
B) We do NOT want the large window icon to be on the left of the logo or the bottom of the letterhead. We are happy having the large window icon to the right or underneath the KB brand.
C) Please use icons for tel, fax and email (e.g. envelope icon for e-mail address)
D) We like two coloured red borders, one at the top and bottom of the letterhead but are happy for variations in shape and size.
E) We currently prefer our address and contact details at the bottom of the letterhead.
F) We like VelloTrine's 'mini window icon' and would prefer this to be used to display the website URL at the bottom right of the letterhead.
G) Please be advised that the letterhead does NOT need additional space for the Company Name as per Pale Forks' submission - the KB brand is sufficient.
Target Market(s)
Owners of high quality property in London.
Industry/Entity Type
Real Estate
Requirements
Must have
- Business Cards: We would like a 'vertical' style business card with our branding on one side and our staff's details on the other;
- Our website is www.korbend.com and we are flexible where that should be on the card and letterhead.
- Stationery details are available in a file attached to this project.
Nice to have
- It would be great to have a horizontal version of the digital logo for placement on property portals (150x60)
Should not have
- Logo should not deviate significantly from the branding on our offices (shop front) - photograph attached.

```html
<!DOCTYPE html>
<html lang="en">
<head>
<meta charset="utf-8">
<title>Korbend Residential – Letterhead</title>
<link rel="stylesheet" href="https://fonts.googleapis.com/css2?family=Signika:wght@400;600;700&display=swap">
<style>
  :root {
    --backdrop: #e9e6e1;
    --paper: #ffffff;
    --brand-red: #a3203a;
    --ink: #1e1e1e;
    --icon-ink: #2b2b2b;
    --window-grey: #e6e6e6;
  }
  * { margin: 0; padding: 0; box-sizing: border-box; }
  html, body {
    width: 1200px; height: 900px; overflow: hidden;
    background: var(--backdrop);
    font-family: "Signika", "Trebuchet MS", sans-serif;
  }
  .letterhead {
    position: absolute; left: 303px; top: 30px;
    width: 594px; height: 840px;
    background: var(--paper);
    box-shadow: 0 2px 10px rgba(0,0,0,.15);
  }
  .heading { position: absolute; left: 40px; top: 52px; color: var(--ink); }
  .heading__title { font-size: 26px; font-weight: 700; line-height: 1; }
  .heading__sub { font-size: 12px; font-weight: 600; margin-top: 4px; }

  .brand {
    position: absolute; right: 30px; top: 0;
    width: 160px; height: 98px;
    background: var(--brand-red);
    color: #fff; text-align: center;
    padding-top: 18px;
  }
  .brand__name { font-size: 17px; font-weight: 400; letter-spacing: .5px; line-height: 1.2; }
  .brand__services { font-size: 9px; font-weight: 600; margin-top: 12px; }

  .contact {
    position: absolute; left: 40px; top: 706px;
    font-size: 11px; line-height: 1.55;
  }
  .contact__address { color: var(--brand-red); margin-bottom: 4px; }
  .contact__line { display: flex; align-items: center; gap: 8px; color: var(--ink); font-weight: 600; }
  .contact__line svg { width: 12px; height: 12px; fill: var(--icon-ink); }
  .contact__web { color: var(--brand-red); font-weight: 600; margin-top: 2px; }

  .registration {
    position: absolute; left: 278px; top: 790px;
    font-size: 9px; color: var(--brand-red);
  }
  .window-mark {
    position: absolute; left: 468px; top: 712px;
    width: 78px; height: 78px;
    background: var(--window-grey);
  }
</style>
</head>
<body>
  <main class="letterhead">
    <header class="heading">
      <h1 class="heading__title">Headline</h1>
      <p class="heading__sub">Sub-headline</p>
    </header>

    <div class="brand">
      <p class="brand__name">KORBEND<br>RESIDENTIAL</p>
      <p class="brand__services">Sales | Lettings | Management</p>
    </div>

    <footer class="contact">
      <p class="contact__address">48 Alder Row,<br>Hampstead, London NW3 2QX</p>
      <p class="contact__line">
        <svg viewBox="0 0 12 12" aria-hidden="true"><path d="M2.5 1l2 2.2-1 1.3c.7 1.5 1.8 2.6 3.3 3.3l1.3-1 2.2 2-1.2 1.7C4.8 10.3 1.7 7.2 1 2.2z"/></svg>
        020 7946 0410
      </p>
      <p class="contact__line">
        <svg viewBox="0 0 12 12" aria-hidden="true"><rect x="3" y="1" width="6" height="3"/><rect x="1" y="4.5" width="10" height="5" rx="1"/><rect x="3" y="8" width="6" height="3"/></svg>
        020 7946 0522
      </p>
      <p class="contact__line">
        <svg viewBox="0 0 12 12" aria-hidden="true"><path d="M1 3h10v6.5H1z M1 3l5 3.6L11 3" fill="var(--icon-ink)"/><path d="M1.5 3.5L6 6.6l4.5-3.1" fill="none" stroke="#fff" stroke-width=".8"/></svg>
        info@korbend.com
      </p>
      <p class="contact__web">www.korbend.com</p>
    </footer>

    <p class="registration">Company Registration No. 05918327</p>
    <div class="window-mark" aria-hidden="true"></div>
  </main>
</body>
</html>
```